Cafeteria management company.. needs fun, healthy, school lunch menu design!

We need a menu design for cafeteria management company.
We manage several cafeterias and need to convey "healthy", "fun", and entice parents and kids to buy from our daily lunch menu.
We are a local company and have great goodwill/name for service.

go to www.bramleymeals.com to see what our company offers...

This menu will be posted online thru all our schools so we want it to look professional as well.
Currently we use it to communicate lots of pertinent information parents and patrons.
We would like to see designs that include all the attached information, and allows content to be editable going forward..(we change meals throughout the year).

Parents of school aged kids. Kids ages 5-18,
Employees of business..

School

• Looking for a usable template with most areas editable...used for high school and elementary menus
Needs to be easily read and use a font that photocopies well and is popular/accessible by all computers..
There is alot of information to include.
Needs to be 1 page 8.5 x 11.
Can be portrait or landscape
Needs to use the trayhopper jpeg.
Like the use of color, but will always be printed in black and white or photocopied as such.

```html
<!DOCTYPE html>
<html lang="en">
<head>
<meta charset="utf-8">
<title>Bramley Meals – Healthy Choice Menu Elementary School 2011/2012</title>
<link href="https://fonts.googleapis.com/css2?family=Arimo:wght@400;700&family=Open+Sans:wght@400;600&display=swap" rel="stylesheet">
<style>
:root{
  --maroon:#9b1b24;
  --red:#d2232a;
  --green:#8dc63f;
  --green-light:#b7dc7a;
  --pink:#f7dcd8;
  --pink-soft:#fbeeec;
  --ink:#1a1a1a;
  --white:#ffffff;
  --page:#2b2b2b;
}
*{box-sizing:border-box;margin:0;padding:0}
html,body{width:1200px;height:900px;overflow:hidden}
body{background:var(--page);font-family:Arimo,Arial,sans-serif;color:var(--ink);position:relative}
.menu-sheet{position:absolute;left:48px;top:55px;width:1104px;height:783px;background:linear-gradient(180deg,var(--white) 0%,var(--pink-soft) 60%,var(--white) 100%);overflow:hidden}
.header-band{position:absolute;left:0;top:0;width:1104px;height:200px}
.food-photos{position:absolute;left:12px;top:5px;width:660px;height:158px;border-radius:14px;background:linear-gradient(90deg,#f3e3d3 0%,#d98a5b 30%,#f1ede4 55%,#8a5a3a 75%,#e9d6b8 100%);opacity:.9}
.contact{position:absolute;left:792px;top:13px;color:var(--white);font-family:"Open Sans",Arial,sans-serif;font-size:12.5px;line-height:16.5px}
.brand-tag{position:absolute;left:760px;top:130px;font-size:19px;color:var(--red)}
.brand-tag small{font-size:12px;color:var(--ink)}
.brand-logo{position:absolute;left:940px;top:100px;width:120px;text-align:center;color:var(--red)}
.brand-logo .mark{display:block;width:38px;height:38px;border-radius:50%;background:var(--red);margin:0 auto 4px}
.brand-logo .name{font-size:16px;font-weight:700;display:block}
.brand-logo .sub{font-size:8px;display:block}
.menu-title{position:absolute;left:262px;top:172px;font-size:15px;font-weight:400;white-space:nowrap}
.menu-title strong{color:var(--red);font-size:18px}

.menu-table{position:absolute;left:30px;top:193px;width:1044px;border-collapse:collapse;table-layout:fixed;border:3px solid var(--maroon)}
.menu-table td,.menu-table th{border-left:2px solid var(--maroon);border-right:2px solid var(--maroon);text-align:center;vertical-align:middle;background:rgba(247,220,216,.75);font-size:11.5px;line-height:13.5px;padding:0 2px}
.menu-table th{background:var(--white);font-size:12.5px;height:20px;position:relative}
.menu-table th .week{position:absolute;left:6px;top:3px;color:var(--red);font-size:12px}
.kettle td{background:var(--green);color:var(--white);font-size:8px;line-height:10px;height:26px}
.week-bar td{background:rgba(230,205,200,.9);height:15px;text-align:left;color:var(--red);font-weight:700;font-size:12px;padding-left:6px}
.meal td{height:60px}
.choice{display:block;font-weight:700;font-size:12.5px;margin-bottom:2px}
.tick{display:inline-block;width:11px;height:11px;vertical-align:-1px;margin-left:3px}
.smile{display:inline-block;width:11px;height:11px;border:1.5px solid var(--ink);border-radius:50%;vertical-align:-1px;margin-left:3px}
.option-head td{background:var(--green);height:26px;line-height:12px}
.option-head .label{color:var(--red);font-size:12.5px;display:block}
.option-head .day{font-weight:700;font-size:11.5px}
.option-body td{height:34px}

.legend{position:absolute;left:30px;top:590px;width:497px;height:33px;border:2px solid var(--ink);background:var(--white);font-size:8.5px;font-weight:700;text-align:center;line-height:13px;padding-top:2px;white-space:nowrap}
.legend .tick,.legend .smile{width:10px;height:10px}
.partners{position:absolute;left:550px;top:590px;width:165px;height:33px;border:2px solid var(--ink);background:var(--white);display:flex;gap:8px;align-items:center;padding-left:6px}
.partners .badge{width:38px;height:24px;border-radius:4px;background:#c7c7c7}
.partners .badge.blue{background:#2f5aa8}
.perks{position:absolute;left:738px;top:588px;width:366px;font-size:9px;font-weight:700;line-height:17px;list-style:none;white-space:nowrap}
.perks li::before{content:"✔";color:var(--maroon);margin-right:5px}
.week-dates{position:absolute;top:631px;height:52px;width:170px;border:2px solid var(--green);background:var(--white);text-align:center;font-size:7.5px;line-height:9.5px;padding:0 3px}
.week-dates h3{color:var(--red);font-size:12px;border-bottom:2px solid var(--green);margin:0 -3px 3px;padding:1px 0}
.cta{position:absolute;top:640px;height:42px;border:2px solid var(--green-light);background:var(--white);font-size:10px;font-weight:700;text-align:center;line-height:13px;padding-top:7px;white-space:nowrap}
.cta .sq{display:block;width:20px;height:20px;background:#2fa9e0;position:absolute;right:6px;top:9px}
.fine{position:absolute;left:8px;top:692px;width:1090px;font-size:8px;line-height:10px}
.fine p{margin-bottom:5px}
.footer-bar{position:absolute;left:0;top:757px;width:1104px;height:26px;background:var(--maroon);color:var(--white);font-weight:700;font-size:14px;line-height:26px;padding-left:32px}
.footer-bar .url{position:absolute;right:56px;top:0;font-weight:400;font-size:12px}
</style>
</head>
<body>
<div class="menu-sheet">
  <svg class="header-band" viewBox="0 0 1104 200" aria-hidden="true">
    <rect width="1104" height="200" fill="#9b1b24"/>
    <path d="M0,188 C320,196 700,150 1104,96 L1104,200 L0,200 Z" fill="#ffffff"/>
  </svg>
  <div class="food-photos" role="img" aria-label="Collage of plated lunch foods: cake, milk, pizza, salads, burger, noodles and a sub sandwich"></div>

  <div class="contact">
    Bramley Food Service Management Inc.<br>
    Ph : 902-555-0147<br>
    E-mail : info@bramleymeals.com<br>
    Address : #114, 28 Harbourview Lane, Bedford NS
  </div>
  <div class="brand-tag"><small>be a </small>Trayhopper</div>
  <div class="brand-logo"><span class="mark"></span><span class="name">Bramley Meals</span><span class="sub">Healthy Food Service Solutions</span></div>

  <h1 class="menu-title">Bramley Meals <strong>HEALTHY CHOICE MENU ELEMENTARY SCHOOL</strong> 2011/2012</h1>

  <table class="menu-table">
    <tr><th><span class="week">Week 1</span>MONDAY</th><th>TUESDAY</th><th>WEDNESDAY</th><th>THURSDAY</th><th>FRIDAY</th></tr>
    <tr class="kettle"><td>From the Kettle......<br>Chicken Veggie Noodle</td><td>From the Kettle......<br>Tomato Vegetable</td><td>From the Kettle......<br>Chicken Rice</td><td>From the Kettle......<br>Corn Chowder</td><td>From the Kettle......<br>Beef Vegetable</td></tr>
    <tr class="meal">
      <td><span class="choice">HEALTHY CHOICE <svg class="tick" viewBox="0 0 11 11"><rect x=".5" y=".5" width="10" height="10" fill="#fff" stroke="#1a1a1a"/><path d="M2 5.5l2.5 2.5L9 2.5" fill="none" stroke="#1a1a1a" stroke-width="1.6"/></svg></span>Pineaple Chicken,Veggi Brown Rice,Stir-Fried Veggies,Milk, Sm. Otameal Cookie</td>
      <td><span class="choice">HEALTHY CHOICE <span class="smile"></span></span>Whole Wheat Spaghetti,Lean Meat or Tomato Sauce, Garlic Roll, Milk, Orange Wedges</td>
      <td><span class="choice">HEALTHY CHOICE</span>2 Pancakes,½ Sliced Ham, Cucumber Slices, Milk, Chocolate Pudding</td>
      <td><span class="choice">HEALTHY CHOICE <span class="smile"></span></span>Mexican Taco Bake,Tossed Garden Salad, Milk, Low-fat Yogurt</td>
      <td><span class="choice">HEALTHY CHOICE</span>Creamy Chicken Pasta, Tossed Garden Salad, Milk, Fresh Fruit Salad</td>
    </tr>
    <tr class="week-bar"><td colspan="5">Week 2</td></tr>
    <tr class="meal">
      <td><span class="choice">HEALTHY CHOICE</span>Homemade Meatloaf,Carrots, Smashed Potatoes, gravy, Milk, ½ Banana</td>
      <td><span class="choice">HEALTHY CHOICE <svg class="tick" viewBox="0 0 11 11"><rect x=".5" y=".5" width="10" height="10" fill="#fff" stroke="#1a1a1a"/><path d="M2 5.5l2.5 2.5L9 2.5" fill="none" stroke="#1a1a1a" stroke-width="1.6"/></svg></span>Turkey Pepperoni Panzaroti, Garden Salad, Milk, Low-fat Yogurt</td>
      <td><span class="choice">HEALTHY CHOICE <svg class="tick" viewBox="0 0 11 11"><rect x=".5" y=".5" width="10" height="10" fill="#fff" stroke="#1a1a1a"/><path d="M2 5.5l2.5 2.5L9 2.5" fill="none" stroke="#1a1a1a" stroke-width="1.6"/></svg></span>Glazed Baked Ham,Smashed Potato, Veggies, Milk, Grapes</td>
      <td><span class="choice">HEALTHY CHOICE <svg class="tick" viewBox="0 0 11 11"><rect x=".5" y=".5" width="10" height="10" fill="#fff" stroke="#1a1a1a"/><path d="M2 5.5l2.5 2.5L9 2.5" fill="none" stroke="#1a1a1a" stroke-width="1.6"/></svg></span>Zesty Italian or Veggie Lasagna, Caesar Salad, Milk, Blueberry Oatmeal Muffin</td>
      <td><span class="choice">HEALTHY CHOICE <svg class="tick" viewBox="0 0 11 11"><rect x=".5" y=".5" width="10" height="10" fill="#fff" stroke="#1a1a1a"/><path d="M2 5.5l2.5 2.5L9 2.5" fill="none" stroke="#1a1a1a" stroke-width="1.6"/></svg></span>Roasted Chicken, Smashed Potato &amp; Veggies, Milk, Orange Wedges</td>
    </tr>
    <tr class="week-bar"><td colspan="5">Week 3</td></tr>
    <tr class="meal">
      <td><span class="choice">HEALTHY CHOICE <svg class="tick" viewBox="0 0 11 11"><rect x=".5" y=".5" width="10" height="10" fill="#fff" stroke="#1a1a1a"/><path d="M2 5.5l2.5 2.5L9 2.5" fill="none" stroke="#1a1a1a" stroke-width="1.6"/></svg></span>Whole Wheat Spaghetti,Lean Meat or Tomato Sauce, Roll, Milk, Apple Crisp</td>
      <td><span class="choice">HEALTHY CHOICE</span>2 Pancakes, ½ Sliced Ham, Milk, Cucumber Slices, Chocolate Pudding</td>
      <td><span class="choice">HEALTHY CHOICE</span>Homemade Goulash, Fresh Garden Salad, Milk, Low-fat Yogurt</td>
      <td><span class="choice">HEALTHY CHOICE</span>Mexican Chicken Enchiladas &amp; Rice, Milk, Banana Oatmeal Muffin</td>
      <td><span class="choice">HEALTHY CHOICE <span class="smile"></span><svg class="tick" viewBox="0 0 11 11"><rect x=".5" y=".5" width="10" height="10" fill="#fff" stroke="#1a1a1a"/><path d="M2 5.5l2.5 2.5L9 2.5" fill="none" stroke="#1a1a1a" stroke-width="1.6"/></svg></span>Roasted Chicken,Smashed Potato &amp; Veggies, Milk, Orange Wedges</td>
    </tr>
    <tr class="week-bar"><td colspan="5">Week 4</td></tr>
    <tr class="meal">
      <td><span class="choice">HEALTHY CHOICE</span>Homemade Chicken Pot Pie, Milk, Grapes</td>
      <td><span class="choice">HEALTHY CHOICE <span class="smile"></span></span>Zesty Italian or Veggie Lasagna, Milk, Caesar Salad, Blueberry Oatmeal Muffin</td>
      <td><span class="choice">HEALTHY CHOICE</span>Grilled Chicken Stir-Fry, Steamed rice, Milk,Apple Sauce</td>
      <td><span class="choice">HEALTHY CHOICE <span class="smile"></span></span>Traditional Shepherd's Pie, Milk, Garden Salad, Fresh Fruit Salad</td>
      <td><span class="choice">HEALTHY CHOICE</span>Creamy Chicken Pasta, Tossed Garden Salad, Milk, Fresh Fruit Salad</td>
    </tr>
    <tr class="option-head">
      <td><span class="label">OPTION MEAL</span><span class="day">Every Monday</span></td>
      <td><span class="label">OPTION MEAL</span><span class="day">Every Tuesday</span></td>
      <td><span class="label">OPTION MEAL</span><span class="day">Every Wednesday</span></td>
      <td><span class="label">OPTION MEAL</span><span class="day">Every Thursday</span></td>
      <td><span class="label">OPTION MEAL</span><span class="day">Every Friday</span></td>
    </tr>
    <tr class="option-body">
      <td>Chopped Chicken Burger, Roasted Potatoes &amp; Veggies, Milk &amp; Dessert</td>
      <td>Cheesy Pizza, Veggies &amp; Dip,<br>Milk &amp; Dessert</td>
      <td>Soft Beef Taco, Mexican Rice,<br>Milk &amp; Dessert</td>
      <td>Pepperoni Pizza, Caesar Salad,<br>Milk &amp; Dessert</td>
      <td>Oven-Baked Chicken Nuggets, Potatoes Wedges, Milk &amp; Dessert</td>
    </tr>
  </table>

  <div class="legend"><span class="smile"></span> = A la carte any smiley-face-meal! <svg class="tick" viewBox="0 0 11 11"><rect x=".5" y=".5" width="10" height="10" fill="#fff" stroke="#1a1a1a"/><path d="M2 5.5l2.5 2.5L9 2.5" fill="none" stroke="#1a1a1a" stroke-width="1.6"/></svg> = Ingredients used are sourced within/in 100 miles of Atlantic Canada<br>* Vegetarian meals are always available, please ask the cafeteria manager.</div>
  <div class="partners"><span class="badge"></span><span class="badge blue"></span></div>

  <ul class="perks">
    <li>Join our email list &amp; get GREAT COUPONS on our healthy meals and snacks!</li>
    <li>Buy your meal plans online &amp; manage your lunch money!</li>
    <li>All names entered into wicked contests. Great prizes available. 100% opt-in.</li>
  </ul>

  <div class="week-dates" style="left:30px"><h3>Week 1</h3>Sept. 1-4, Oct. 5-9, Nov. 2-6, Nov.30-Dec4, Jan. 4-7, Feb. 1-5, Mar. 1-5, April 26-30, May 24-28, June21-25</div>
  <div class="week-dates" style="left:202px"><h3>Week 2</h3>Sept. 1-4, Oct. 12-16, Nov.9-13, Dec. 7-11, Jan. 11-14, Feb. 8-12, Mar.8-12, April5-9, May 3-7,May 31- June 4</div>
  <div class="week-dates" style="left:374px"><h3>Week 3</h3>Sept. 1-4, Oct. 19-23, Nov. 16-20, Dec. 14-18, Jan. 18-22, Feb. 15-19, Mar. 15-19, April 12-16, May 10-14, June 7-11</div>
  <div class="week-dates" style="left:546px"><h3>Week 4</h3>Sept. 1-4, Oct. 26-30, Nov. 23-27, Dec. 21-25, Jan. 25-29, Feb. 22-26, April 19-23, May 17-21, June 14-18</div>

  <div class="cta" style="left:733px;width:177px">win FREE LUNCH FOR A MONTH!<br>Sign-up today! ;-)</div>
  <div class="cta" style="left:914px;width:184px;text-align:left;padding-left:8px">Follow us and be fed well!<br>@trayhopper on<span class="sq"></span></div>

  <div class="fine">
    <p><strong>Healthy Meal Plan: Buy online at:</strong> www.bramleymeals.com, or by cheque. The meal plan may be purchased weekly or monthly. Please make cheque payable to: Bramley Food Service. See the Cafeteria Manager for details on meal plan purchase. Unused tickets/meals are valid until the end of the current school year. Non-consecutive days are allowed. Purchase 5 or more meals and receive a 20 cent discount per meal, when the plan is purchased weekly / monthly. Menu dates as per meal served, are subject to change. Please contact cafeteria manager for mea/date confirmation.</p>
    <p><strong>Healthy Choice Menu:</strong> Variations may occur due to differences in suppliers, ingredients substitutions, recipe revisions, meal assembly at the cafeteria, and/or seasons of the year. Certain menu items may not be available at all locations. We encourage anyone with food allergies, sensitivities or special dietary needs to contact/notify the cafeteria manager. We will work with you the very best we can. Bramley Food Service Management Inc. and its employees do not assume responsibility for a particular allergy or sensitivity to any foods provided in any of our cafeterias.</p>
  </div>

  <div class="footer-bar">If you have a great coupon idea or comment, please let us know! Email us at &nbsp;: Trayhopper@bramleymeals.com<span class="url">www.bramleymeals.com</span></div>
</div>
</body>
</html>
```